Business Card for Web Design consulting firm

Business card designs for Web Design consulting firm

Target Market(s)

English speaking adults ages 30 - 60. Predominantly professional services eg. Doctor, Dentist

Industry/Entity Type

Consulting

Requirements
Must have
• Double sided card

```html
<!DOCTYPE html>
<html lang="en">
<head>
<meta charset="utf-8">
<title>Norvello Business Card</title>
<link rel="stylesheet" href="https://fonts.googleapis.com/css2?family=Open+Sans:wght@400;600;700&display=swap">
<style>
  :root {
    --ink: #4a4a4a;
    --orange: #f79c26;
    --card: #f6f7f6;
    --page: #ffffff;
    --white: #ffffff;
    --text: #1c1c1c;
  }
  html, body {
    margin: 0;
    padding: 0;
    width: 848px;
    height: 1200px;
    overflow: hidden;
    background: var(--page);
  }
  .card {
    position: absolute;
    left: 104px;
    width: 644px;
    height: 377px;
    display: block;
    font-family: "Open Sans", sans-serif;
  }
  .card--front { top: 157px; }
  .card--back { top: 658px; }
  .card-bg { fill: var(--card); }
  .brand-name {
    fill: var(--ink);
    font-weight: 600;
    font-size: 25px;
    letter-spacing: 4px;
  }
  .brand-dot { fill: var(--orange); }
  .person-name { fill: var(--ink); font-weight: 700; font-size: 18.5px; }
  .person-role { fill: var(--orange); font-weight: 400; font-size: 12px; }
  .contact { font-size: 12.3px; fill: var(--text); }
  .contact-label { fill: var(--orange); }
  .band-text {
    fill: var(--white);
    font-weight: 700;
    dominant-baseline: central;
    text-anchor: middle;
  }
  .band-text--tagline { font-size: 20px; }
  .band-text--web { font-size: 16.5px; }
</style>
</head>
<body>

<svg class="card card--front" viewBox="0 0 452 265" role="group" aria-label="Business card front">
  <defs>
    <linearGradient id="frontTone" x1="0" y1="0" x2="1" y2="0">
      <stop offset="0" stop-color="#4a4a4a"/>
      <stop offset="1" stop-color="#f79c26"/>
    </linearGradient>
  </defs>
  <rect class="card-bg" x="0" y="0" width="452" height="265"/>
  <circle class="brand-dot" cx="34" cy="97" r="11"/>
  <text class="brand-name" x="54" y="106">NORVELLO</text>

  <text class="person-name" x="298" y="60">Daniel Harper</text>
  <text class="person-role" x="298" y="77">Sales Person</text>

  <text class="contact" x="22" y="172"><tspan class="contact-label">Address</tspan> 42 Example Lane, Brisbane, 4000</text>
  <text class="contact" x="22" y="189"><tspan class="contact-label">Phone</tspan> 07 55501234</text>
  <text class="contact" x="22" y="206"><tspan class="contact-label">Mobile</tspan> 0400555123</text>
  <text class="contact" x="22" y="223"><tspan class="contact-label">Email</tspan> hello@norvello.com</text>
  <text class="contact" x="22" y="240"><tspan class="contact-label">Website</tspan> www.norvello.com</text>

  <rect x="300" y="200" width="152" height="65" fill="url(#frontTone)" role="img" aria-label="Decorative brand graphic in charcoal and orange"/>
</svg>

<svg class="card card--back" viewBox="0 0 452 265" role="group" aria-label="Business card back">
  <defs>
    <linearGradient id="backTone" x1="0" y1="0" x2="1" y2="1">
      <stop offset="0" stop-color="#4a4a4a"/>
      <stop offset="0.55" stop-color="#6a5a44"/>
      <stop offset="1" stop-color="#f79c26"/>
    </linearGradient>
  </defs>
  <rect class="card-bg" x="0" y="0" width="452" height="265"/>
  <text class="brand-name" x="20" y="42">NORVELLO</text>

  <rect x="0" y="70" width="200" height="195" fill="url(#backTone)" opacity="0.18" role="img" aria-label="Decorative brand graphic in charcoal and orange"/>
  <rect x="200" y="0" width="252" height="265" fill="url(#backTone)" role="img" aria-label="Decorative brand graphic in charcoal and orange"/>

  <text class="band-text band-text--tagline" x="316" y="158" transform="rotate(-51.7 316 158)">web design consulting</text>
  <text class="band-text band-text--web" x="389" y="182" transform="rotate(-51.7 389 182)">www.norvello.com</text>
</svg>

</body>
</html>
```